We need a business card design for a Dubai based company .

We need a business card for a Dubai based company called "Zernova Smoking Requisites Trading LLC". We mainly import Flavoured Tobacco products and Charcoal which is used for smoking in a Hookah/Shisha and distribute to the wholesalers and retailers. Logo file is attached herewith.

```html
<!DOCTYPE html>
<html lang="en">
<head>
<meta charset="utf-8">
<title>Zernova Smoking Requisites Trading LLC — Business Card</title>
<link href="https://fonts.googleapis.com/css2?family=Exo+2:wght@400;600&family=Roboto:wght@400&display=swap" rel="stylesheet">
<style>
  :root {
    --backdrop: #2a2a2a;
    --brand-red: #ab2b2e;
    --brand-red-deep: #9c2427;
    --card-white: #f1f1f1;
    --card-white-shade: #e4e4e4;
    --ink: #2a2a2a;
    --on-red: #f4f4f4;
  }
  * { margin: 0; padding: 0; box-sizing: border-box; }
  html, body {
    width: 1200px; height: 1138px; overflow: hidden;
    background: var(--backdrop);
  }
  .canvas { position: relative; width: 1200px; height: 1138px; }

  .card {
    position: absolute;
    border-radius: 16px;
  }
  .card--front {
    left: 274px; top: 186px; width: 623px; height: 376px;
    background: linear-gradient(160deg, var(--brand-red) 0%, var(--brand-red) 55%, var(--brand-red-deep) 100%);
    display: flex; align-items: center; justify-content: center;
  }
  .card--back {
    left: 276px; top: 608px; width: 618px; height: 374px;
    background: linear-gradient(180deg, var(--card-white) 0%, var(--card-white-shade) 100%);
    color: var(--ink);
    font-family: "Roboto", sans-serif;
  }

  .wordmark {
    font-family: "Exo 2", sans-serif;
    font-weight: 400;
    letter-spacing: 0.12em;
    text-transform: uppercase;
    line-height: 1;
  }
  .wordmark--front { color: var(--on-red); font-size: 46px; }
  .wordmark--back {
    position: absolute; left: 338px; top: 88px;
    width: 236px; text-align: center;
    color: var(--ink); font-size: 34px;
  }

  .holder { position: absolute; left: 37px; top: 198px; }
  .holder__name {
    font-family: "Exo 2", sans-serif; font-weight: 600;
    font-size: 24px; color: var(--brand-red); letter-spacing: 0.01em;
  }
  .holder__role { font-size: 16px; margin-top: 2px; }

  .contacts { position: absolute; left: 38px; top: 274px; list-style: none; }
  .contacts li {
    display: flex; align-items: center; gap: 12px;
    font-size: 16.5px; height: 24px;
  }
  .contacts svg { width: 15px; height: 15px; fill: var(--brand-red); }

  .address {
    position: absolute; right: 35px; top: 298px;
    text-align: right; font-size: 16.5px; line-height: 24px;
  }
</style>
</head>
<body>
<main class="canvas">
  <section class="card card--front">
    <span class="wordmark wordmark--front">Zernova</span>
  </section>

  <section class="card card--back">
    <span class="wordmark wordmark--back">Zernova</span>

    <div class="holder">
      <p class="holder__name">KARIM HADDAD</p>
      <p class="holder__role">Managing Director</p>
    </div>

    <ul class="contacts">
      <li>
        <svg viewBox="0 0 16 16" aria-hidden="true"><path d="M1 6c0-2 3-3.5 7-3.5S15 4 15 6v1h-3.5V5.5h-7V7H1zM4 8h8l2 5v1H2v-1zm4 1.5a2 2 0 1 0 0 4 2 2 0 0 0 0-4z"/></svg>
        000-111-0000
      </li>
      <li>
        <svg viewBox="0 0 16 16" aria-hidden="true"><path d="M1 3h14v10H1zm1.5 1.5v.3L8 9l5.5-4.2v-.3zm0 2.2v4.8h11V6.7L8 10.9z"/></svg>
        karim@zernova.com
      </li>
      <li>
        <svg viewBox="0 0 16 16" aria-hidden="true"><path d="M8 1a7 7 0 1 0 0 14A7 7 0 0 0 8 1zm0 1.5c.8 0 1.7 1.5 2 3.8H6c.3-2.3 1.2-3.8 2-3.8zM5.9 2.9c-.6 1-.9 2.2-1 3.4H2.6a5.5 5.5 0 0 1 3.3-3.4zm4.2 0a5.5 5.5 0 0 1 3.3 3.4h-2.3c-.1-1.2-.4-2.4-1-3.4zM2.6 9.7h2.3c.1 1.2.4 2.4 1 3.4a5.5 5.5 0 0 1-3.3-3.4zm3.4 0h4c-.3 2.3-1.2 3.8-2 3.8s-1.7-1.5-2-3.8zm5.1 0h2.3a5.5 5.5 0 0 1-3.3 3.4c.6-1 .9-2.2 1-3.4zM2.5 7.3h2.4v1.4H2.5zm3.4 0h4.2v1.4H5.9zm5.2 0h2.4v1.4h-2.4z"/></svg>
        www.zernova.com
      </li>
    </ul>

    <p class="address">P.O Box 00000,<br>Dubai, Emirates</p>
  </section>
</main>
</body>
</html>
```